Buchcover-Design für Roman
Zielgruppe
Ich bin Autor und veröffentliche meinen ersten Roman.
Eine humoristische Geschichte voller Musik und Filmzitate.
Die Zielgruppe sind Erwachsene zwischen 30 und 40.
Aufgabenstellung
Titel: Der Alltag bleibt doch bloß ein Spiel
Autor: Konrad Marelstein
Bitte unbedingt auch die technischen Vorgaben beachten, siehe auch die Musterdatei, die ich hochgeladen habe.(Cover.PNG)
Technische Daten des Verlages:
Das Buch soll als Paperback und als Ebook gleichzeitig im KXL-Verlag erscheinen.
Das Paperback soll das Format 12 * 19 cm haben, also jeweils die Vorderseite und Rückseite.
Es werden ca. 380 Seiten dabei herauskommen.
Ich gehe von ca. 2,5 cm für den Buchrücken aus.
Laut Verlag muss die Farbdatei mindestens 300 dpi haben.
Das Format beträgt laut KXL: 275,1 mm * 200,0 mm .
Zusätzlich muss auf die Rückseite ein Barcode als PNG Datei eingefügt werden, der 144 dpi haben wird.
Vorläufiger Klappentext:
Malte Hinrichs, für seine Freunde, wenn er denn noch welche hätte, einfach nur Hinni, ist ein nerdiger Verlierertyp, der in eine tiefe Sinnkrise stürzt. Verantwortlich dafür sind 3 Dinge, sein nahender 40. Geburtstag, der Tod seines Vaters und die Einladung zum Klassentreffen seiner alten Schule. Bisher hat er in seinem Leben noch nicht viel hinbekommen und sich auch deshalb von den Menschen entfernt. Er führt ein einsames Dasein, in seiner begrenzten Welt aus Filmen und Musik. Nun, auch mit 39 noch lange nicht erwachsen, muss er sich diesen Dingen stellen und sein Leben endlich auf die Reihe bekommen, wobei er natürlich von einer Katastrophe in die nächste stürzt.
Vorläufige Autoreninfo:
Der Autor wurde 1979 in Dortmund geboren und lebt seit 2017 mit seiner Familie in seiner Wahlheimat, dem beschaulichen Kempen am Niederrhein. Er ist hauptberuflich bei einem großen Finanzdienstleistungsunternehmen in Düsseldorf tätig, verwirklichte sich zu seinem 40. Geburtstag seinen lang gehegten Traum und begann nebenberuflich zu schreiben. Das hier vorliegende Produkt seiner Phantasie stellt seinen 1. Roman dar. Weitere sind in Planung.
Soll beides auf die Rückseite gedruck..

```html
<!DOCTYPE html>
<html lang="de">
<head>
<meta charset="utf-8">
<title>Der Alltag bleibt doch bloß ein Spiel – Buchumschlag</title>
<link rel="stylesheet" href="https://fonts.googleapis.com/css2?family=Roboto:wght@400;700&family=Nunito:wght@400&family=Luckiest+Guy&display=swap">
<style>
  :root {
    --rust: #b33c00;
    --cream: #f6e8cf;
    --cream-soft: #efd7b6;
    --skin: #f2b07f;
    --ink: #111111;
    --spine-line: #f0c9a4;
    --barcode-field: #ffffff;
  }
  html, body {
    margin: 0;
    padding: 0;
    width: 1200px;
    height: 860px;
    overflow: hidden;
    background: var(--rust);
  }
  .cover {
    position: relative;
    width: 1200px;
    height: 860px;
    background: var(--rust);
    color: var(--cream);
    font-family: "Roboto", Arial, sans-serif;
  }
  /* Back cover */
  .back {
    position: absolute;
    left: 0;
    top: 0;
    width: 543px;
    height: 860px;
  }
  .blurb {
    position: absolute;
    left: 34px;
    width: 468px;
    text-align: center;
    font-size: 15.6px;
    line-height: 22.4px;
    margin: 0;
  }
  .blurb h2 {
    font-size: 15.6px;
    font-weight: 700;
    margin: 0;
  }
  .blurb p { margin: 0; }
  .blurb--book { top: 40px; }
  .blurb--author { top: 353px; }
  .barcode-field {
    position: absolute;
    left: 317px;
    top: 711px;
    width: 190px;
    height: 104px;
    background: var(--barcode-field);
  }
  .illustration {
    position: absolute;
  }
  .illustration--back {
    left: 48px;
    top: 606px;
    width: 136px;
    height: 254px;
    border-radius: 68px 68px 30px 30px;
    background: linear-gradient(180deg, var(--cream-soft) 0%, var(--cream-soft) 42%, var(--skin) 50%, var(--ink) 62%, var(--ink) 100%);
  }
  /* Spine */
  .spine {
    position: absolute;
    left: 543px;
    top: 0;
    width: 113px;
    height: 860px;
    border-left: 1px solid var(--spine-line);
    border-right: 1px solid var(--spine-line);
    box-sizing: border-box;
  }
  .spine-lettering {
    position: absolute;
    left: 0;
    top: 0;
    width: 111px;
    height: 860px;
  }
  .spine-lettering text {
    font-family: "Roboto", Arial, sans-serif;
    font-size: 25px;
    fill: var(--cream);
  }
  .illustration--spine {
    left: 18px;
    top: 690px;
    width: 80px;
    height: 170px;
    border-radius: 40px 40px 16px 16px;
    background: linear-gradient(180deg, var(--cream-soft) 0%, var(--cream-soft) 40%, var(--skin) 48%, var(--ink) 58%, var(--ink) 100%);
  }
  /* Front cover */
  .front {
    position: absolute;
    left: 656px;
    top: 0;
    width: 544px;
    height: 860px;
  }
  .front-author {
    position: absolute;
    top: 26px;
    left: 0;
    width: 544px;
    text-align: center;
    font-family: "Nunito", Arial, sans-serif;
    font-size: 34px;
    letter-spacing: 1px;
    margin: 0;
    font-weight: 400;
  }
  .illustration--front {
    left: 60px;
    top: 90px;
    width: 410px;
    height: 770px;
    border-radius: 205px 205px 60px 60px;
    background: linear-gradient(180deg, var(--cream-soft) 0%, var(--cream-soft) 44%, var(--skin) 52%, var(--ink) 62%, var(--ink) 100%);
  }
  .title {
    position: absolute;
    left: 0;
    top: 0;
    width: 544px;
    height: 860px;
  }
  .title text {
    font-family: "Luckiest Guy", "Arial Black", Impact, sans-serif;
    fill: var(--cream);
  }
  .title .word-big { filter: drop-shadow(3px 4px 3px rgba(40, 10, 0, 0.55)); }
  .title .word-small { filter: drop-shadow(2px 2px 2px rgba(40, 10, 0, 0.5)); }
</style>
</head>
<body>
<div class="cover">

  <section class="back">
    <div class="blurb blurb--book">
      <h2>Das Buch:</h2>
      <p>Malte Hinrichs, für seine Freunde, wenn er denn noch welche hätte, einfach nur Hinni, ist ein nerdiger Verlierertyp, der in eine tiefe Sinnkrise stürzt. Verantwortlich dafür sind 3 Dinge, sein nahender 40. Geburtstag, der Tod seines Vaters und die Einladung zum Klassentreffen seiner alten Schule. Bisher hat er in seinem Leben noch nicht viel hinbekommen und sich auch deshalb von den Menschen entfernt. Er führt ein einsames Dasein, in seiner begrenzten Welt aus Filmen und Musik. Nun, auch mit 39 noch lange nicht erwachsen, muss er sich diesen Dingen stellen und sein Leben endlich auf die Reihe bekommen, wobei er natürlich von einer Katastrophe in die nächste stürzt.</p>
    </div>
    <div class="blurb blurb--author">
      <h2>Der Autor:</h2>
      <p>Der Autor wurde 1979 in Dortmund geboren und lebt seit 2017 mit seiner Familie in seiner Wahlheimat, dem beschaulichen Kempen am Niederrhein. Er ist hauptberuflich bei einem großen Finanzdienstleistungsunternehmen in Düsseldorf tätig, verwirklichte sich zu seinem 40. Geburtstag seinen lang gehegten Traum und begann nebenberuflich zu schreiben. Das hier vorliegende Produkt seiner Phantasie stellt seinen 1. Roman dar. Weitere sind in Planung.</p>
    </div>
    <div class="illustration illustration--back" role="img" aria-label="Kleine Figur mit Filmspule als Kopf, die mit der Hand das Rockzeichen zeigt"></div>
    <div class="barcode-field" aria-hidden="true"></div>
  </section>

  <section class="spine">
    <svg class="spine-lettering" viewBox="0 0 111 860" aria-label="Der Alltag bleibt doch bloß ein Spiel – Konrad Marelstein">
      <text transform="translate(65 388) rotate(-90)" textLength="350" lengthAdjust="spacingAndGlyphs">Der Alltag bleibt doch bloß ein Spiel</text>
      <text transform="translate(65 652) rotate(-90)" textLength="226" lengthAdjust="spacingAndGlyphs">Konrad Marelstein</text>
    </svg>
    <div class="illustration illustration--spine" role="img" aria-label="Kleine Figur mit Filmspule als Kopf"></div>
  </section>

  <section class="front">
    <h1 class="front-author">Konrad Marelstein</h1>
    <div class="illustration illustration--front" role="img" aria-label="Figur im schwarzen T-Shirt mit großer Filmspule als Kopf, Hand zeigt das Rockzeichen"></div>
    <svg class="title" viewBox="0 0 544 860" aria-label="Der Alltag bleibt doch bloß ein Spiel">
      <text class="word-small" x="86" y="567" font-size="58" textLength="104" lengthAdjust="spacingAndGlyphs">Der</text>
      <text class="word-big" x="44" y="704" font-size="160" textLength="456" lengthAdjust="spacingAndGlyphs">ALLTAG</text>
      <text class="word-small" x="44" y="763" font-size="42" textLength="166" lengthAdjust="spacingAndGlyphs">bleibt doch</text>
      <text class="word-small" x="46" y="806" font-size="42" textLength="150" lengthAdjust="spacingAndGlyphs">bloß ein</text>
      <text class="word-big" x="226" y="822" font-size="120" textLength="284" lengthAdjust="spacingAndGlyphs">SPIEL</text>
    </svg>
  </section>

</div>
</body>
</html>
```